Business Card Design for a Lending Business (Hard Money loans)

We need a business card for our Real Estate Lending business. We do hard Money loans for real estate investors. We have an existing logo we like, see attached. I'd like the business card to mostly include the logo colors, but a bright color pop of some sort would be nice to see also. Card should include Logo, Company Name, Company Address, Employee Name, Cell Phone, Main Phone, Email, Website

Industry/Entity Type

Finance / Lending

Contact Information for Business Card

Logo, Company Name, Company Address, Employee Name, Cell Phone, Main Phone, Email, Website

Requirements
Nice to have
• I'd like the business card to mostly include the logo colors, but a bright color pop of some sort would be nice to see also.

```html
<!DOCTYPE html>
<html lang="en">
<head>
<meta charset="utf-8">
<title>Ridgeline Lending – Business Card</title>
<link rel="stylesheet" href="https://fonts.googleapis.com/css2?family=Lato:wght@400;700&display=swap">
<style>
  :root {
    --backdrop: #d8d8d8;
    --card-black: #050505;
    --card-white: #ffffff;
    --navy: #0b2a8f;
    --sky: #00aee3;
    --rule: #d4d4d4;
  }
  * { margin: 0; padding: 0; box-sizing: border-box; }
  html, body {
    width: 1200px; height: 900px; overflow: hidden;
    background: var(--backdrop);
    font-family: "Lato", sans-serif;
  }
  .sheet {
    position: relative; width: 1200px; height: 900px;
    display: flex; align-items: center; justify-content: center; gap: 60px;
  }
  .card {
    position: relative; width: 520px; height: 300px; overflow: hidden;
    box-shadow: 0 18px 30px rgba(0,0,0,0.18);
  }
  .card--front { background: var(--card-black); display: flex; align-items: center; justify-content: center; }
  .card--back { background: var(--card-white); }

  .brand { display: flex; align-items: center; gap: 12px; }
  .brand__dot { width: 26px; height: 26px; border-radius: 50%; background: var(--sky); flex: none; }
  .brand__name {
    font-weight: 700; font-size: 30px; letter-spacing: 2px; line-height: 1.1;
    text-transform: uppercase; color: var(--sky);
  }
  .card--back .brand__name { color: var(--navy); font-size: 22px; letter-spacing: 1.5px; }
  .card--back .brand__dot { background: var(--navy); width: 20px; height: 20px; }

  .back__brand { position: absolute; left: 26px; top: 110px; width: 196px; }
  .back__divider { position: absolute; left: 236px; top: 40px; width: 1px; height: 130px; background: var(--rule); }

  .contact { position: absolute; left: 252px; top: 40px; list-style: none; color: var(--navy); font-size: 11px; line-height: 1.3; }
  .contact__item { display: flex; align-items: flex-start; gap: 8px; margin-bottom: 10px; }
  .contact__icon { width: 10px; height: 10px; flex: none; margin-top: 2px; fill: var(--sky); }

  .waves { position: absolute; inset: 0; width: 520px; height: 300px; }
</style>
</head>
<body>
<main class="sheet">
  <section class="card card--front" aria-label="Card front">
    <div class="brand">
      <span class="brand__dot"></span>
      <span class="brand__name">Ridgeline Lending</span>
    </div>
  </section>

  <section class="card card--back" aria-label="Card back">
    <svg class="waves" viewBox="0 0 520 300" aria-hidden="true">
      <path fill="var(--sky)" d="M300,300 C400,285 450,220 475,150 C490,95 500,50 520,30 L520,300 Z"/>
      <path fill="var(--navy)" d="M250,300 C370,292 425,220 448,150 C462,100 478,50 508,14 C490,50 478,100 466,150 C440,230 380,290 290,300 Z"/>
    </svg>

    <div class="back__brand">
      <div class="brand">
        <span class="brand__dot"></span>
        <span class="brand__name">Ridgeline<br>Lending</span>
      </div>
    </div>

    <div class="back__divider"></div>

    <ul class="contact">
      <li class="contact__item">
        <svg class="contact__icon" viewBox="0 0 10 10"><path d="M5 0a3.5 3.5 0 0 0-3.5 3.5C1.5 6 5 10 5 10s3.5-4 3.5-6.5A3.5 3.5 0 0 0 5 0zm0 5a1.4 1.4 0 1 1 0-2.8A1.4 1.4 0 0 1 5 5z"/></svg>
        <span>1250 Harlow Lane<br>Millbrook, MD 21000</span>
      </li>
      <li class="contact__item">
        <svg class="contact__icon" viewBox="0 0 10 10"><path d="M2 0.5l2 2-1 1.2c.6 1.3 1.6 2.3 2.9 2.9L7.1 5.5l2 2-1.2 1.8C4.3 9.2.8 5.7.6 2z"/></svg>
        <span>410-555-0142</span>
      </li>
      <li class="contact__item">
        <svg class="contact__icon" viewBox="0 0 10 10"><path d="M0 2h10v6H0z"/></svg>
        <span>info@RidgelineLending.com</span>
      </li>
      <li class="contact__item">
        <svg class="contact__icon" viewBox="0 0 10 10"><circle cx="5" cy="5" r="5"/></svg>
        <span>www.ridgelinelending.com/</span>
      </li>
    </ul>
  </section>
</main>
</body>
</html>
```